Harbrook Techlink Solutions

We need a Logo and Website for our company based in London. We are a IT recruitment company . We provide quality resources to top IT company across UK.

Industry/Entity Type

It Company

Number of Pages Required

4 page

```html
<!DOCTYPE html>
<html lang="en">
<head>
<meta charset="utf-8">
<title>Harbrook Techlink Solutions</title>
<link rel="stylesheet" href="https://fonts.googleapis.com/css2?family=Montserrat:wght@400;500;600&family=Open+Sans:wght@400;600;700&family=Roboto+Condensed:wght@400;700&display=swap">
<style>
:root{
  --green:#0b9e7f;
  --green-dark:#08886d;
  --ink:#222;
  --text:#444;
  --muted:#777;
  --black:#000;
  --footer:#2b2b2b;
  --footer-line:#3d3d3d;
  --white:#fff;
  --card-border:#e2e2e2;
}
*{margin:0;padding:0;box-sizing:border-box}
html,body{width:1200px;height:2413px;overflow:hidden}
body{position:relative;background:var(--white);font-family:"Open Sans",Arial,sans-serif;color:var(--text)}
.abs{position:absolute}

/* header */
.site-header{position:absolute;left:0;top:0;width:1200px;height:121px;background:var(--white)}
.brand{position:absolute;left:48px;top:30px;font-family:"Montserrat",Arial,sans-serif;font-weight:500;color:var(--green);font-size:25px;line-height:31px;letter-spacing:.5px;text-transform:uppercase}
.call{position:absolute;left:1026px;top:14px;text-align:left}
.call-label{font-size:10px;font-weight:600;color:#333;letter-spacing:.3px}
.call-number{font-family:"Montserrat",Arial,sans-serif;font-size:19px;font-weight:500;color:var(--green);margin-top:1px}
.main-nav a{position:absolute;top:48px;height:73px;line-height:73px;font-family:"Montserrat",Arial,sans-serif;font-size:12px;font-weight:600;color:#333;text-decoration:none;letter-spacing:.6px;text-align:center}
.main-nav a.active{background:var(--green);color:var(--white)}

/* hero */
.hero{position:absolute;left:0;top:121px;width:1200px;height:664px;background:linear-gradient(100deg,#3c3d3f 0%,#5f6163 35%,#4a4c4e 60%,#2c2d2f 100%)}
.hero-line1{position:absolute;left:71px;top:177px;font-family:"Roboto Condensed",Arial,sans-serif;font-size:54px;color:var(--white);letter-spacing:5px}
.hero-line2{position:absolute;left:71px;top:245px;font-family:"Roboto Condensed",Arial,sans-serif;font-weight:700;font-size:66px;color:var(--green);letter-spacing:-.5px}
.hero-line3{position:absolute;left:71px;top:322px;font-family:"Roboto Condensed",Arial,sans-serif;font-size:46px;color:var(--white)}
.dot{position:absolute;width:14px;height:14px;border-radius:50%;background:var(--white)}
.dot.on{background:var(--green)}

/* features */
.features{position:absolute;left:0;top:785px;width:1200px;height:204px;background:var(--black)}
.feature{position:absolute;top:741px;width:260px;text-align:center}
.feature-icon{width:84px;height:84px;border-radius:50%;background:var(--green);margin:0 auto;display:flex;align-items:center;justify-content:center}
.feature-icon.light{background:var(--white)}
.feature h3{font-size:16px;font-weight:400;color:var(--green);margin-top:27px}
.feature p{font-size:12px;color:var(--white);line-height:17px;margin-top:4px;padding:0 12px}
.feature .more{display:inline-block;font-size:11px;font-weight:600;color:var(--white);margin-top:10px;letter-spacing:.3px}
.feature .more.green{color:var(--green)}

/* welcome */
.welcome-rule{position:absolute;top:1066px;height:1px;background:#bbb}
.welcome-title{position:absolute;left:0;top:1048px;width:1200px;text-align:center;font-family:"Montserrat",Arial,sans-serif;font-size:27px;color:var(--ink)}
.welcome-title span{color:var(--green)}
.welcome-text{position:absolute;left:100px;top:1110px;width:1000px;text-align:center;font-size:12px;line-height:21px;color:var(--muted)}
.btn{position:absolute;display:flex;align-items:center;justify-content:center;font-size:11px;font-weight:600;letter-spacing:.3px;text-decoration:none}
.btn-solid{background:var(--green);color:var(--white)}
.btn-outline{border:1px solid var(--green);color:var(--green);background:var(--white)}

/* services */
.service-card{position:absolute;top:1335px;width:362px;height:357px;border:3px solid var(--card-border);background:var(--white)}
.service-photo{position:absolute;left:8px;top:10px;width:340px;height:199px}
.service-card h4{position:absolute;left:8px;top:230px;font-size:14px;font-weight:700;color:var(--ink)}
.service-card h4.green{color:var(--green)}
.service-card p{position:absolute;left:8px;top:258px;width:340px;font-size:12px;line-height:17px;color:#333}

/* split band */
.split-photo{position:absolute;left:0;top:1734px;width:545px;height:325px;background:radial-gradient(circle at 55% 45%,#9fd3ff 0%,#3b6fd1 30%,#14285e 70%,#0b1530 100%)}
.split-panel{position:absolute;left:545px;top:1734px;width:655px;height:325px;background:var(--green)}
.split-list{position:absolute;left:636px;top:1808px;list-style:none}
.split-list li{position:relative;font-size:15px;color:var(--white);line-height:28px;padding-left:20px}
.split-list li::before{content:"";position:absolute;left:0;top:11px;width:7px;height:7px;border-radius:50%;background:var(--white)}
.ring{position:absolute;width:14px;height:14px;border-radius:50%;border:1.5px solid var(--white)}
.ring.on{background:var(--white)}

/* footer */
.site-footer{position:absolute;left:0;top:2059px;width:1200px;height:269px;background:var(--footer)}
.footer-rule{position:absolute;top:2093px;width:1px;height:200px;background:var(--footer-line)}
.footer-heading{position:absolute;top:2094px;font-family:"Montserrat",Arial,sans-serif;font-size:17px;color:var(--green)}
.footer-text{position:absolute;font-size:12px;line-height:17px;color:var(--white)}
.email-input{position:absolute;left:521px;top:2202px;width:298px;height:36px;background:var(--white);font-size:11px;color:#999;padding:10px 13px}
.loc-item{position:absolute;left:943px;font-size:12px;line-height:17px;color:var(--white)}
.loc-item svg{position:absolute;left:0;top:3px}
.loc-item span{display:block;margin-left:22px}

/* bottom bar */
.bottom-bar{position:absolute;left:0;top:2328px;width:1200px;height:85px;background:var(--green)}
.legal-links{position:absolute;left:0;top:2352px;width:1200px;text-align:center;font-size:11px;color:var(--white);font-weight:600}
.copyright{position:absolute;left:0;top:2374px;width:1200px;text-align:center;font-size:11px;color:var(--white)}
.social{position:absolute;top:2344px;width:29px;height:29px;border:1.5px solid var(--white)}
.social.fill{background:var(--white)}
</style>
</head>
<body>

<header class="site-header">
  <div class="brand">Harbrook Techlink<br>Solutions</div>
  <div class="call">
    <div class="call-label">CALL ME NOW</div>
    <div class="call-number">123-456-7890</div>
  </div>
  <nav class="main-nav">
    <a class="active" style="left:430px;width:86px">HOME</a>
    <a style="left:548px;width:96px">ABOUT US</a>
    <a style="left:682px;width:90px">SERVICES</a>
    <a style="left:805px;width:80px">GALLERY.</a>
    <a style="left:930px;width:70px">BLOG</a>
    <a style="left:1036px;width:110px">CONTACTS US</a>
  </nav>
</header>

<section class="hero" role="img" aria-label="Close-up photo of hands typing on a laptop keyboard"></section>
<div class="hero-line1">WE WILL</div>
<div class="hero-line2">SHOW YOU THE WAY</div>
<div class="hero-line3">TO SUCCESS!</div>
<span class="dot on" style="left:61px;top:638px"></span>
<span class="dot" style="left:83px;top:638px"></span>
<span class="dot" style="left:107px;top:638px"></span>

<section class="features"></section>
<div class="feature" style="left:52px">
  <div class="feature-icon light">
    <svg width="36" height="36" viewBox="0 0 36 36"><rect x="6" y="9" width="24" height="20" rx="2" fill="none" stroke="#0b9e7f" stroke-width="3"/><line x1="6" y1="15" x2="30" y2="15" stroke="#0b9e7f" stroke-width="3"/></svg>
  </div>
  <h3>Vestibulum Iaculis</h3>
  <p>Lorem ipsum dolor sit amet, consectetur ipsum dolor sit amet, consectetur adipis do edit</p>
  <span class="more green">MORE ▸</span>
</div>
<div class="feature" style="left:328px">
  <div class="feature-icon">
    <svg width="36" height="36" viewBox="0 0 36 36" fill="none" stroke="#fff" stroke-width="2.6" stroke-linejoin="round"><rect x="6" y="16" width="6" height="13"/><path d="M12 17 L17 8 Q20 7 20 11 L19 15 H27 Q30 15 29 19 L27 27 Q26 29 23 29 H12"/></svg>
  </div>
  <h3>Fusce Euismod</h3>
  <p>Lorem ipsum dolor sit amet, consectetur ipsum dolor sit amet, consectetur adipis do edit</p>
  <span class="more">MORE ▸</span>
</div>
<div class="feature" style="left:605px">
  <div class="feature-icon">
    <svg width="36" height="36" viewBox="0 0 36 36" fill="none" stroke="#fff" stroke-width="2.6"><circle cx="18" cy="18" r="11"/><path d="M18 11 V18 H23"/></svg>
  </div>
  <h3>Fusce Euismod</h3>
  <p>Lorem ipsum dolor sit amet, consectetur ipsum dolor sit amet, consectetur adipis do edit</p>
  <span class="more">MORE ▸</span>
</div>
<div class="feature" style="left:888px">
  <div class="feature-icon">
    <svg width="36" height="36" viewBox="0 0 36 36" fill="#fff"><circle cx="18" cy="12" r="6"/><path d="M7 29 Q7 19 18 19 Q29 19 29 29 Z"/></svg>
  </div>
  <h3>Proin Dictum Elem</h3>
  <p>Lorem ipsum dolor sit amet, consectetur ipsum dolor sit amet, consectetur adipis do edit</p>
  <span class="more">MORE ▸</span>
</div>

<div class="welcome-rule" style="left:48px;width:242px"></div>
<div class="welcome-rule" style="left:906px;width:246px"></div>
<h2 class="welcome-title">WELCOME TO <span>HARBROOK TECHLINK SOLUTIONS</span></h2>
<p class="welcome-text">Lorem ipsum dolor sit amet, consectetur adipiscing elit, sed do eiusmod tempor incididunt ut labore et dolore magna aliqua. Ut enim ad minim veniam, quis nostrud exercitation ullamco laboris nisi ut aliquip ex ea commodo consequat. Duis aute irure dolor in reprehenderit in voluptate velit esse cillum dolore eu fugiat nulla pariatur. Excepteur sint occaecat cupidatat non proident, sunt in culpa qui officia deserunt mollit anim id est laborum.</p>
<a class="btn btn-solid" style="left:529px;top:1190px;width:142px;height:45px">READ MORE</a>

<article class="service-card" style="left:46px">
  <div class="service-photo" role="img" aria-label="Photo of a hand holding a tablet with floating digital marketing icons" style="background:linear-gradient(135deg,#0b3f86,#2f8fd8 55%,#bfe3f7)"></div>
  <h4 class="green">INTERNET MARKETING</h4>
  <p>Lorem ipsum dolor sit amet, consectetur adipiscing elit, sed do eiusmod tempor incididunt</p>
  <a class="btn btn-solid" style="left:8px;top:302px;width:97px;height:34px">READ MORE</a>
</article>
<article class="service-card" style="left:420px">
  <div class="service-photo" role="img" aria-label="Photo of a hand reaching towards a stream of floating image panels" style="background:linear-gradient(135deg,#1f4f9a,#6aa8e0 50%,#dfe9f3)"></div>
  <h4>WEB DEVELOPMENT</h4>
  <p>Lorem ipsum dolor sit amet, consectetur adipiscing elit, sed do eiusmod tempor incididunt</p>
  <a class="btn btn-outline" style="left:8px;top:302px;width:97px;height:34px">READ MORE</a>
</article>
<article class="service-card" style="left:793px">
  <div class="service-photo" role="img" aria-label="Photo of a golden padlock resting on a dark keyboard" style="background:linear-gradient(135deg,#2a2a2a,#555 45%,#8a7a3e 70%,#3a3a3a)"></div>
  <h4>WEBSITE PROTECTION</h4>
  <p>Lorem ipsum dolor sit amet, consectetur adipiscing elit, sed do eiusmod tempor incididunt</p>
  <a class="btn btn-outline" style="left:8px;top:302px;width:97px;height:34px">READ MORE</a>
</article>

<div class="split-photo" role="img" aria-label="Photo of hands on a glowing keyboard beneath a global network of connections"></div>
<div class="split-panel"></div>
<ul class="split-list">
  <li>Lorem ipsum dolor sit amet, consectetur adipiscing elit,</li>
  <li>Sed do eiusmod tempor incididunt ut labore et dolore magna aliqua.</li>
  <li>Ut enim ad minim veniam, quis nostrud exercitation ullamco laboris</li>
  <li>Nisi ut aliquip ex ea commodo consequat.</li>
  <li>Duis aute irure dolor in reprehenderit in voluptate</li>
</ul>
<span class="ring" style="left:800px;top:1994px"></span>
<span class="ring on" style="left:826px;top:1994px"></span>
<span class="ring" style="left:851px;top:1994px"></span>

<footer class="site-footer"></footer>
<div class="footer-rule" style="left:465px"></div>
<div class="footer-rule" style="left:883px"></div>

<h5 class="footer-heading" style="left:56px">ABOUT US</h5>
<p class="footer-text" style="left:50px;top:2136px;width:366px">Lorem ipsum dolor sit amet, consectetur adipiscing elit, sed do eiusmod tempor incididunt ut labore et dolore magna aliqua. Ut enim ad minim veniam, quis nostrud exercitation ullamco laboris nisi ut aliquip ex ea commodo consequat. Duis aute irure dolor in reprehenderit in voluptate velit esse cillum dolore eu fugiat nulla pariatur.</p>
<a class="btn btn-solid" style="left:51px;top:2268px;width:105px;height:37px">READ MORE</a>

<h5 class="footer-heading" style="left:520px">NEWSLETTER SIGNUP</h5>
<p class="footer-text" style="left:520px;top:2136px;width:310px">Subscribe our newsletter to know our daily updates and offer daily updates and offerpsun dolor sit amet elit, sed aliqua.</p>
<div class="email-input">Enter your Email Id</div>
<a class="btn btn-solid" style="left:521px;top:2249px;width:298px;height:37px;font-size:13px">SUBSCRIBE</a>

<h5 class="footer-heading" style="left:943px">LOCATION</h5>
<div class="loc-item" style="top:2143px">
  <svg width="11" height="14" viewBox="0 0 11 14"><path d="M5.5 0 A5.5 5.5 0 0 1 11 5.5 C11 9 5.5 14 5.5 14 C5.5 14 0 9 0 5.5 A5.5 5.5 0 0 1 5.5 0 Z" fill="#0b9e7f"/><circle cx="5.5" cy="5.5" r="2" fill="#2b2b2b"/></svg>
  <span>Company Name<br>Address Line 1, Address Line 2<br>Country - 123456</span>
</div>
<div class="loc-item" style="top:2200px">
  <svg width="12" height="12" viewBox="0 0 12 12"><path d="M2 0 L4.5 0 L5.5 3 L4 4.5 Q5 7 7.5 8 L9 6.5 L12 7.5 L12 10 Q12 12 10 12 Q0 11 0 2 Q0 0 2 0 Z" fill="#0b9e7f"/></svg>
  <span>Office: (123-456-7890)</span>
</div>
<div class="loc-item" style="top:2224px">
  <svg width="12" height="10" viewBox="0 0 12 10"><rect x="0" y="0" width="12" height="10" fill="#0b9e7f"/><path d="M0.5 0.8 L6 5.5 L11.5 0.8" stroke="#2b2b2b" stroke-width="1.2" fill="none"/></svg>
  <span>info@companyname.com</span>
</div>

<div class="bottom-bar"></div>
<div class="legal-links">Policies &nbsp;|&nbsp; Privacy &nbsp;|&nbsp; Terms &amp; Conditions &nbsp;|&nbsp; Disclaimer &nbsp;|&nbsp; Site Map</div>
<div class="copyright">Copyright 2016 Comapny name. All Rights Reserved.</div>
<span class="social" style="left:1049px" aria-label="Professional network"></span>
<span class="social fill" style="left:1086px" aria-label="Microblog"></span>
<span class="social" style="left:1123px" aria-label="Social network"></span>

</body>
</html>
```